Communication and Marketing agency needs a new presentation card

We are a group of communication and marketing agencies specialized in companies that are in the logistics and industrial sector. The head agency is TELVANO Grupo and the group consists of 4 agencies: TELVANO Media, TELVANO Digital, TELVANO Research and EnlazaPorImagen. We hace 4 offices in Spain (Madrid, Barcelona, Valencia and Murcia). We are looking for a clean and attractive design that transmits our experience, brand presence in the market and knowledge to those who receive the card.It has to maintain the colors of the logo that is attached.
Target Market(s)
logistics and industrial sector
Marketing department
Clean and attractive design

```html
<!DOCTYPE html>
<html lang="es">
<head>
<meta charset="utf-8">
<title>EnlazaPorImagen — Business Card</title>
<link href="https://fonts.googleapis.com/css2?family=Questrial&display=swap" rel="stylesheet">
<style>
  :root {
    --paper: #f8f8fa;
    --red: #c0202e;
    --charcoal: #3a3a3d;
    --ink: #141414;
    --white: #ffffff;
  }
  * { margin: 0; padding: 0; box-sizing: border-box; }
  html, body {
    width: 1200px;
    height: 686px;
    overflow: hidden;
    background: var(--paper);
  }
  .card {
    position: relative;
    width: 1200px;
    height: 686px;
    background: var(--paper);
    font-family: "Questrial", "Century Gothic", sans-serif;
    color: var(--ink);
    overflow: hidden;
  }
  .card__bands {
    position: absolute;
    inset: 0;
    width: 1200px;
    height: 686px;
  }
  .brand {
    position: absolute;
    left: 60px;
    top: 256px;
    color: var(--red);
    font-size: 74px;
    line-height: 80px;
    letter-spacing: 1px;
    text-transform: uppercase;
    white-space: nowrap;
  }
  .person {
    position: absolute;
    left: 620px;
    top: 156px;
    white-space: nowrap;
  }
  .person__name {
    color: var(--red);
    font-size: 46px;
    line-height: 54px;
    font-weight: 400;
  }
  .person__role {
    font-size: 36px;
    line-height: 42px;
    font-weight: 400;
  }
  .divider {
    position: absolute;
    left: 626px;
    top: 262px;
    width: 357px;
    height: 2px;
    background: var(--red);
  }
  .contacts {
    position: absolute;
    left: 580px;
    top: 288px;
    list-style: none;
  }
  .contact {
    display: flex;
    align-items: flex-start;
    font-size: 33px;
    line-height: 40px;
    margin-bottom: 22px;
    white-space: nowrap;
  }
  .contact__icon {
    width: 30px;
    height: 30px;
    margin-top: 6px;
    margin-right: 20px;
    flex: none;
    fill: var(--red);
  }
</style>
</head>
<body>
<main class="card">
  <svg class="card__bands" viewBox="0 0 1400 800" preserveAspectRatio="none" aria-hidden="true">
    <polygon fill="var(--charcoal)" points="962,0 1400,0 1400,448"/>
    <polygon fill="var(--white)" points="1005,0 1033,0 1372,336 1356,352"/>
    <polygon fill="var(--red)" points="915,0 962,0 1195,240 1195,290"/>
    <polygon fill="var(--charcoal)" points="0,488 0,800 312,800"/>
    <polygon fill="var(--white)" points="76,618 65,634 230,800 262,800"/>
    <polygon fill="var(--red)" points="86,545 120,545 362,800 320,800"/>
  </svg>

  <div class="brand">EnlazaPor<br>Imagen</div>

  <header class="person">
    <h1 class="person__name">Pablo Rueda</h1>
    <p class="person__role">Director</p>
  </header>
  <div class="divider"></div>

  <ul class="contacts">
    <li class="contact">
      <svg class="contact__icon" viewBox="0 0 30 30" aria-hidden="true">
        <rect x="9" y="2" width="14" height="26" rx="2.5"/>
        <rect x="11.5" y="5.5" width="9" height="17" fill="var(--paper)"/>
        <circle cx="16" cy="25" r="1.3" fill="var(--paper)"/>
        <path d="M3 14 q0 -4 6 -4 v10 q-6 0 -6 -4z"/>
      </svg>
      <span>0555 01 48270</span>
    </li>
    <li class="contact">
      <svg class="contact__icon" viewBox="0 0 30 30" aria-hidden="true">
        <rect x="1" y="6" width="28" height="19"/>
        <path d="M2 7 L15 17 L28 7" fill="none" stroke="var(--paper)" stroke-width="2"/>
        <path d="M2 24 L11 15 M28 24 L19 15" fill="none" stroke="var(--paper)" stroke-width="1.5"/>
      </svg>
      <span>info@enlazaporimg.com</span>
    </li>
    <li class="contact">
      <svg class="contact__icon" viewBox="0 0 30 30" aria-hidden="true">
        <circle cx="15" cy="16" r="12"/>
        <path d="M5 16 H25" stroke="var(--paper)" stroke-width="1.5"/>
      </svg>
      <span>www.enlazaporimg.com</span>
    </li>
    <li class="contact">
      <svg class="contact__icon" viewBox="0 0 30 30" aria-hidden="true">
        <path d="M15 2 a7 7 0 0 1 7 7 c0 5 -7 12 -7 12 s-7 -7 -7 -12 a7 7 0 0 1 7 -7z"/>
        <circle cx="15" cy="9" r="2.6" fill="var(--paper)"/>
        <path d="M2 19 H8 M22 19 H28 L28 28 H2 Z" fill="none" stroke="var(--red)" stroke-width="1.8"/>
      </svg>
      <span>2204/56 calle norte,<br>madrid 28010</span>
    </li>
  </ul>
</main>
</body>
</html>
```